2014 Card

I need a vertical business card designed to incorporate 2 Companies in wheaton IL. First company is dew ray lens (I always type this with no caps and in Cataneo BT font. I like the way the L and the P surround the i) This is a Photography company that does Wedding Photography, Portraiture, Sunset, and many other types of Photography. The website is www.dewraylens.example
The other company is Grand Kiosk Max a Photo Booth rental Company. We rent photo booths to weddings and all types of events. The end project should mainly appeal to Brides and show Class. I have added 2 files One is the Grand Kiosk Max Logo and the other is on dew ray lenss header on the website. I do Like the eye in the sky on the dew ray lens file

Target Market(s)

Future brides

Industry/Entity Type

Business

Requirements
Must have
• Grand Kiosk Max part should say A Photo Booth Rental Company
dew ray lens should say All in one photography studio and address should be on this side,

```html
<!DOCTYPE html>
<html lang="en">
<head>
<meta charset="utf-8">
<title>dew ray lens – Business Card</title>
<link href="https://fonts.googleapis.com/css2?family=Alegreya:ital,wght@1,400;1,500;1,700&display=swap" rel="stylesheet">
<style>
  :root {
    --page: #ffffff;
    --card-dark: #4e4a42;
    --ink: #1e1d1b;
    --ink-soft: #5a5650;
    --cream: #f4efe4;
    --icon: #c9bda6;
    --gold: #b8935e;
    --sand: #e6ded0;
    --ribbon: #efeae0;
  }
  * { margin: 0; padding: 0; box-sizing: border-box; }
  html, body {
    width: 1200px; height: 900px; overflow: hidden;
    background: var(--page);
    font-family: "Alegreya", Georgia, serif;
    font-style: italic;
  }
  .canvas { position: relative; width: 1200px; height: 900px; }

  /* Front card */
  .card-front {
    position: absolute; left: 201px; top: 115px;
    width: 368px; height: 617px;
    background: linear-gradient(180deg, #f7f4ee 0%, #ffffff 45%, #fbf8f3 100%);
    box-shadow: 0 0 3px rgba(0,0,0,0.18);
    overflow: hidden;
  }
  .film-decor {
    position: absolute; left: 0; top: 0; width: 368px; height: 240px;
    background: radial-gradient(ellipse at 70% 30%, #e4ddd0 0%, #efeae1 45%, rgba(255,255,255,0) 80%);
  }
  .swirl-decor {
    position: absolute; left: 0; top: 350px; width: 368px; height: 239px;
    background:
      radial-gradient(ellipse at 85% 20%, #b89260 0%, rgba(184,146,96,0) 45%),
      radial-gradient(ellipse at 20% 80%, #d7c2a0 0%, rgba(215,194,160,0) 55%),
      linear-gradient(160deg, #faf6ef 0%, #e9dcc6 50%, #c9a977 100%);
  }
  .front-bar {
    position: absolute; left: 0; bottom: 0; width: 100%; height: 28px;
    background: var(--card-dark);
  }
  .brand-name {
    position: absolute; left: 0; width: 100%; top: 222px;
    text-align: center; font-size: 54px; font-weight: 700;
    color: var(--ink); letter-spacing: -0.5px;
  }
  .brand-tagline {
    position: absolute; left: 0; width: 100%; top: 310px;
    text-align: center; font-size: 16px; font-weight: 500;
    color: var(--ink-soft);
  }
  .partner-name {
    position: absolute; left: 0; width: 100%; top: 466px;
    text-align: center; font-size: 34px; font-weight: 500;
    color: #55504a;
  }
  .partner-ribbon {
    position: absolute; left: 57px; top: 524px; width: 250px; height: 20px;
    background: var(--ribbon);
    clip-path: polygon(0 0, 100% 0, 96% 50%, 100% 100%, 0 100%, 4% 50%);
  }
  .partner-tagline {
    position: absolute; left: 0; width: 100%; top: 522px;
    text-align: center; font-size: 15px; font-weight: 500;
    color: var(--ink-soft);
  }

  /* Back card */
  .card-back {
    position: absolute; left: 638px; top: 163px;
    width: 363px; height: 617px;
    background: var(--card-dark);
    box-shadow: 2px 3px 5px rgba(0,0,0,0.35);
  }
  .contact-row { position: absolute; left: 0; width: 100%; }
  .contact-icon { position: absolute; left: 52px; }
  .contact-text {
    position: absolute; left: 124px;
    color: var(--cream); font-size: 14px; line-height: 18px;
    letter-spacing: 0.2px;
  }
  .contact-text.phone { font-size: 16px; letter-spacing: 0.6px; }
  .social-mark {
    position: absolute; left: 56px; width: 24px; height: 24px;
    background: var(--icon); border-radius: 3px;
  }
</style>
</head>
<body>
<main class="canvas">

  <section class="card-front" aria-label="Card front">
    <div class="film-decor" role="img" aria-label="Faint film strip decoration"></div>
    <div class="swirl-decor" role="img" aria-label="Soft golden swirl of light"></div>
    <h1 class="brand-name">dew ray lens</h1>
    <p class="brand-tagline">All in one photography studio</p>
    <h2 class="partner-name">Grand Kiosk Max</h2>
    <div class="partner-ribbon"></div>
    <p class="partner-tagline">A Photo Booth rental company</p>
    <div class="front-bar"></div>
  </section>

  <section class="card-back" aria-label="Card back">
    <div class="contact-row" style="top:278px">
      <svg class="contact-icon" width="28" height="28" viewBox="0 0 28 28" aria-hidden="true">
        <path d="M14 3 L26 14 L22 14 L22 26 L6 26 L6 14 L2 14 Z" fill="var(--icon)"/>
        <rect x="11.5" y="18" width="5" height="8" fill="var(--card-dark)"/>
      </svg>
      <p class="contact-text">58 Orchard Lane<br>Springvale IL 60999</p>
    </div>

    <div class="contact-row" style="top:335px">
      <svg class="contact-icon" width="28" height="28" viewBox="0 0 28 28" aria-hidden="true">
        <rect x="8" y="2" width="12" height="24" rx="2.5" fill="none" stroke="var(--icon)" stroke-width="2"/>
        <rect x="10.5" y="6" width="7" height="14" fill="var(--icon)"/>
      </svg>
      <p class="contact-text phone">555-014-2277</p>
    </div>

    <div class="contact-row" style="top:387px">
      <svg class="contact-icon" width="28" height="28" viewBox="0 0 28 28" aria-hidden="true">
        <path d="M5 12 L14 5 L23 12 L23 24 L5 24 Z" fill="var(--icon)"/>
        <path d="M5 12 L14 18 L23 12" fill="none" stroke="var(--card-dark)" stroke-width="1.6"/>
      </svg>
      <p class="contact-text">hello@grandkioskmax.example</p>
    </div>

    <div class="contact-row" style="top:432px">
      <svg class="contact-icon" width="28" height="28" viewBox="0 0 28 28" aria-hidden="true">
        <rect x="8" y="3" width="12" height="22" rx="6" fill="none" stroke="var(--icon)" stroke-width="1.8"/>
        <line x1="14" y1="3" x2="14" y2="11" stroke="var(--icon)" stroke-width="1.6"/>
      </svg>
      <p class="contact-text">www.dewraylens.example</p>
    </div>

    <div class="contact-row" style="top:513px">
      <span class="social-mark"></span>
      <p class="contact-text" style="top:2px">@dewraylens</p>
    </div>
  </section>

</main>
</body>
</html>
```